QLindex warden tap - styling

We have a prototyped single page application. The content is in place what we need is restyling to

- make it more user friendly
- modern look and feel
- improve accessibility features
- use our brand guidelines (screen shots attached of the full website)

Prototype is available at http://boardviewapp.examplehost.net/

Target form factor:
Primary - tablet
Secondary - desktop

Target Market(s)

Business users - not financial professionals but people working for big companies who have some limited training in the concepts

Number of Pages Required

1 page

Requirements
Must have
• Touch user interface

```html
<!DOCTYPE html>
<html lang="en">
<head>
<meta charset="utf-8">
<title>QLindex warden tap – Flight Plan</title>
<link href="https://fonts.googleapis.com/css2?family=Open+Sans:wght@400;600;700&display=swap" rel="stylesheet">
<style>
:root{
  --brand:#0b5fb3;
  --brand-dark:#084f99;
  --brand-deep:#06468a;
  --rule:#2a74c0;
  --ink:#111;
  --muted:#9a9a9a;
  --axis:#dcdcdc;
  --accent-blue:#2f7fd0;
  --accent-orange:#e8693a;
  --fill-blue:#f2f7fc;
  --fill-orange:#f8e7e1;
  --tip:#2c2c2c;
  --white:#fff;
}
*{box-sizing:border-box;margin:0;padding:0}
html,body{width:1200px;height:729px;overflow:hidden;background:var(--white);font-family:"Open Sans",Arial,sans-serif;color:var(--ink)}
.app{position:relative;width:1200px;height:729px}
.topbar{position:absolute;left:0;top:0;width:1200px;height:37px;background:var(--brand);border-bottom:1px solid var(--brand-deep)}
.brand-name{position:absolute;left:22px;top:3px;font-size:25px;font-weight:700;color:var(--white);letter-spacing:.2px}
.menu-toggle{position:absolute;left:152px;top:12px}
.account-select{position:absolute;left:1040px;top:10px;width:84px;height:17px;background:#3b86d2;border-radius:2px;font-size:8px;font-weight:700;color:var(--white);padding:3px 0 0 7px}
.account-select svg{position:absolute;right:6px;top:5px}
.top-icon{position:absolute;top:12px}
.sidebar{position:absolute;left:0;top:37px;width:144px;height:661px;background:var(--brand)}
.nav-item{display:block;height:40px;border-bottom:1px solid var(--rule);font-size:8px;font-weight:700;color:var(--white);padding:16px 0 0 17px;text-decoration:none}
.nav-item.is-active{height:32px;background:var(--brand-dark);border-left:3px solid #5da0e6;padding:15px 0 0 14px}
.page-head{position:absolute;left:144px;top:37px;width:1056px;height:52px;border-bottom:1px solid #e6e6e6}
.page-title{position:absolute;left:32px;top:17px;font-size:15px;font-weight:700}
.kpi{position:absolute;top:0;width:144px;height:52px;border-left:1px solid #e2e2e2;background:linear-gradient(#fff 55%,#efefef);padding:12px 0 0 14px}
.kpi-value{font-size:15px;font-weight:700;color:var(--brand);line-height:1}
.kpi-label{font-size:5.5px;color:#aaa;margin-top:3px;letter-spacing:.2px}
.chart{position:absolute;left:0;top:0}
.slider{position:absolute;top:523px;width:320px;text-align:center}
.slider-title{font-size:15px;font-weight:700}
.slider-track{position:relative;margin-top:11px;height:21px;border-radius:11px;background:linear-gradient(#f4f6f8,#d7dde3);border:1px solid #c5ccd3}
.slider-fill{position:absolute;left:5px;right:5px;top:5px;height:9px;border-radius:5px;background:linear-gradient(#2e74c6,#0b4f9c)}
.slider-knob{position:absolute;top:-6px;width:30px;height:30px;border-radius:50%;background:radial-gradient(circle at 50% 35%,#fff,#dfe6ee);border:1px solid #c3ccd6}
.slider-labels{position:relative;height:14px;margin-top:11px;font-size:10px;font-weight:600}
.slider-labels .min{position:absolute;left:4px}
.slider-labels .max{position:absolute;right:0}
.slider-labels .value{position:absolute;left:0;right:0;top:-2px;color:var(--brand)}
.footer{position:absolute;left:0;top:698px;width:1200px;height:31px;background:var(--brand);border-top:1px solid var(--brand-deep)}
.footer a{position:absolute;top:13px;font-size:7.5px;font-weight:600;color:#d8e7f7;text-decoration:none}
</style>
</head>
<body>
<div class="app">
  <header class="topbar">
    <div class="brand-name">QLindex</div>
    <svg class="menu-toggle" width="26" height="12" viewBox="0 0 26 12" aria-label="Toggle menu"><path d="M6 1 1 6l5 5" fill="none" stroke="#fff" stroke-width="2"/><rect x="10" y="0" width="14" height="2" fill="#fff"/><rect x="10" y="5" width="14" height="2" fill="#fff"/><rect x="10" y="10" width="14" height="2" fill="#fff"/></svg>
    <div class="account-select">ZYX<svg width="8" height="5" viewBox="0 0 8 5"><path d="M1 1l3 3 3-3" fill="none" stroke="#fff" stroke-width="1.5"/></svg></div>
    <svg class="top-icon" style="left:1143px" width="9" height="10" viewBox="0 0 9 10" aria-label="Profile"><circle cx="4.5" cy="3" r="2.5" fill="#9cc4ee"/><path d="M0 10c0-3 2-4.5 4.5-4.5S9 7 9 10z" fill="#9cc4ee"/></svg>
    <svg class="top-icon" style="left:1179px" width="9" height="10" viewBox="0 0 9 10" aria-label="Lock"><path d="M2 5V3a2.5 2.5 0 0 1 5 0v2" fill="none" stroke="#9cc4ee" stroke-width="1.3"/><rect x="0" y="5" width="9" height="5" fill="#9cc4ee"/></svg>
  </header>

  <nav class="sidebar">
    <a class="nav-item is-active" href="#">DASHBOARD</a>
    <a class="nav-item" href="#">ANALYTICS</a>
    <a class="nav-item" href="#">RISK</a>
    <a class="nav-item" href="#">ALM</a>
    <a class="nav-item" href="#">OPTIMIZER</a>
    <a class="nav-item" href="#">CURVES</a>
    <a class="nav-item" href="#">ADMIN</a>
  </nav>

  <section class="page-head">
    <h1 class="page-title">Flight Plan</h1>
    <div class="kpi" style="left:483px"><div class="kpi-value">91%</div><div class="kpi-label">FUNDING LEVEL</div></div>
    <div class="kpi" style="left:627px"><div class="kpi-value">-1.7%</div><div class="kpi-label">FUNDING LEVEL CHANGE</div></div>
    <div class="kpi" style="left:771px"><div class="kpi-value">3%</div><div class="kpi-label">PROGRESS AGAINST FLIGHT PLAN</div></div>
    <div class="kpi" style="left:915px"><div class="kpi-value">67%</div><div class="kpi-label">5YR PROJECTED FUNDING LEVEL</div></div>
  </section>

  <svg class="chart" width="1200" height="520" viewBox="0 0 1200 520" role="img" aria-label="Flight plan funding level chart">
    <g stroke="#e9e9e9" stroke-width="1">
      <line x1="182" y1="127" x2="1167" y2="127"/><line x1="182" y1="198" x2="1167" y2="198"/>
      <line x1="182" y1="268" x2="1167" y2="268"/><line x1="182" y1="338" x2="1167" y2="338"/>
      <line x1="182" y1="409" x2="1167" y2="409"/>
    </g>
    <path fill="var(--fill-blue)" d="M182,373 C220,373 220,374 259,374 C302,374 302,272 346,272 C386,272 386,267 426,267 C466,267 466,287 507,287 C546,287 546,225 586,225 C631,225 631,122 676,122 C719,122 719,205 762,205 C805,205 805,231 848,231 C888,231 888,178 929,178 C968,178 968,197 1008,197 C1048,197 1048,266 1089,266 C1122,266 1122,258 1155,258 L1167,252 L1167,507 L182,507 Z"/>
    <path fill="var(--fill-orange)" d="M182,385 C220,385 220,421 260,421 C303,421 303,457 346,457 C386,457 386,458 426,458 C466,458 466,401 507,401 C546,401 546,331 586,331 C631,331 631,302 676,302 C719,302 719,317 762,317 C805,317 805,357 848,357 C888,357 888,384 929,384 C968,384 968,378 1008,378 C1048,378 1048,327 1089,327 C1122,327 1122,272 1155,272 L1167,262 L1167,507 L182,507 Z"/>
    <g font-family="Open Sans, Arial, sans-serif" font-size="16" fill="var(--axis)">
      <text x="198" y="133">160%</text><text x="198" y="204">140%</text><text x="198" y="274">120%</text>
      <text x="198" y="344">100%</text><text x="198" y="415">80%</text><text x="198" y="487">60%</text>
      <g text-anchor="middle">
        <text x="292" y="487">30/NOV/13</text><text x="412" y="487">01/FEB/14</text><text x="527" y="487">01/ABR/14</text>
        <text x="643" y="487">01/JUN/14</text><text x="738" y="487">2014</text><text x="790" y="487">2015</text>
        <text x="843" y="487">2016</text><text x="896" y="487">2017</text><text x="949" y="487">2018</text>
        <text x="1002" y="487">2019</text><text x="1055" y="487">2020</text><text x="1107" y="487">2021</text>
      </g>
    </g>
    <path fill="none" stroke="var(--accent-blue)" stroke-width="1.3" d="M182,373 C220,373 220,374 259,374 C302,374 302,272 346,272 C386,272 386,267 426,267 C466,267 466,287 507,287 C546,287 546,225 586,225 C631,225 631,122 676,122 C719,122 719,205 762,205 C805,205 805,231 848,231 C888,231 888,178 929,178 C968,178 968,197 1008,197 C1048,197 1048,266 1089,266 C1122,266 1122,258 1155,258 L1167,252"/>
    <path fill="none" stroke="var(--accent-orange)" stroke-width="1.3" d="M182,385 C220,385 220,421 260,421 C303,421 303,457 346,457 C386,457 386,458 426,458 C466,458 466,401 507,401 C546,401 546,331 586,331 C631,331 631,302 676,302 C719,302 719,317 762,317 C805,317 805,357 848,357 C888,357 888,384 929,384 C968,384 968,378 1008,378 C1048,378 1048,327 1089,327 C1122,327 1122,272 1155,272 L1167,262"/>
    <g fill="#fff" stroke="var(--accent-blue)" stroke-width="2">
      <circle cx="259" cy="374" r="5.5"/><circle cx="346" cy="272" r="5.5"/><circle cx="426" cy="267" r="5.5"/>
      <circle cx="507" cy="287" r="5.5"/><circle cx="586" cy="225" r="5.5"/><circle cx="676" cy="122" r="5.5"/>
      <circle cx="762" cy="205" r="5.5"/><circle cx="848" cy="231" r="5.5"/><circle cx="929" cy="178" r="5.5"/>
      <circle cx="1008" cy="197" r="5.5"/><circle cx="1089" cy="266" r="5.5"/><circle cx="1155" cy="258" r="5.5"/>
    </g>
    <g fill="#fff" stroke="var(--accent-orange)" stroke-width="2">
      <circle cx="260" cy="421" r="5.5"/><circle cx="346" cy="457" r="5.5"/><circle cx="426" cy="458" r="5.5"/>
      <circle cx="507" cy="401" r="5.5"/><circle cx="586" cy="331" r="7"/><circle cx="676" cy="302" r="5.5"/>
      <circle cx="762" cy="317" r="5.5"/><circle cx="848" cy="357" r="5.5"/><circle cx="929" cy="384" r="5.5"/>
      <circle cx="1008" cy="378" r="5.5"/><circle cx="1089" cy="327" r="5.5"/><circle cx="1155" cy="272" r="5.5"/>
    </g>
    <g class="tooltip">
      <path d="M486,229 H679 V310 H594 L586,318 L578,310 H486 Z" fill="var(--tip)" fill-opacity=".93"/>
      <line x1="486" y1="266" x2="679" y2="266" stroke="#555"/>
      <text x="588" y="262" text-anchor="middle" font-family="Open Sans, Arial, sans-serif" font-size="17" fill="#a9a9a9">12 Abr 2014</text>
      <text x="563" y="290" text-anchor="middle" font-family="Open Sans, Arial, sans-serif" font-size="23" font-weight="700" fill="#fff">98%</text>
    </g>
  </svg>

  <div class="slider" style="left:258px">
    <div class="slider-title">Investment Strategy</div>
    <div class="slider-track"><div class="slider-fill"></div><div class="slider-knob" style="left:142px"></div></div>
    <div class="slider-labels"><span class="min">Matching</span><span class="value" style="left:-2px">50% / 50%</span><span class="max">Growth</span></div>
  </div>
  <div class="slider" style="left:780px">
    <div class="slider-title">Investment Strategy</div>
    <div class="slider-track"><div class="slider-fill"></div><div class="slider-knob" style="left:142px"></div></div>
    <div class="slider-labels"><span class="min">£0m</span><span class="value">£15.0m</span><span class="max">£30m</span></div>
  </div>

  <footer class="footer">
    <a href="#" style="left:27px">HELP</a>
    <a href="#" style="left:85px">ABOUT US</a>
    <a href="#" style="left:170px">TERM AND CONDITIONS</a>
    <a href="#" style="left:327px">CONTACT US</a>
  </footer>
</div>
</body>
</html>
```